Business card design for upmarket Home Technology design and Installation company

Hello designers, we need a great business card designed.
We need it to convey high tech, and also sophistication .
We work with some of the most affluent people in the world building them home technology systems, and A/V entertainment systems.

Services offered include the following:
Design, sales, installation, and maintenance of

*Home Automation systems
*Distributed / Multi-Room Audio and Video
*High Performance Networks & WiFi
* Lighting and Shade Control
*Home cinema
*Security and CCTV Systems

I have included a copy of our logo to use for your design efforts.

Target Market(s)

Upmarket clients with multi million euro villas.

Industry/Entity Type

Home technology

Contact Information for Business Card

NAME: Derek Halloran ADDRESS: Plaza Brisa Local 42, Port Velamar, 07392 PHONE: +34-602-518-794 EMAIL: DHalloran@VELTRAsmarthomes.com WEB: www.veltrasmarthomes.com

Requirements
Must have
• Our Logo, and our tagline

```html
<!DOCTYPE html>
<html lang="en">
<head>
<meta charset="utf-8">
<title>VELTRA Clever Living — Business Card</title>
<link rel="stylesheet" href="https://fonts.googleapis.com/css2?family=Montserrat:wght@300;400;500;700&display=swap">
<style>
  :root {
    --backdrop: #cbfbf7;
    --card-navy: #012439;
    --pattern-teal: #3f8f9c;
    --pattern-deep: #0b3a4d;
    --gold: #c9a448;
    --white: #ffffff;
    --silver: #dfe8ee;
  }
  * { margin: 0; padding: 0; box-sizing: border-box; }
  html, body {
    width: 1200px; height: 760px; overflow: hidden;
    background: var(--backdrop);
    font-family: "Montserrat", sans-serif;
  }
  .canvas { position: relative; width: 1200px; height: 760px; }
  .card {
    position: absolute; left: 75px; top: 75px;
    width: 1050px; height: 600px;
    background: var(--card-navy);
    box-shadow: 0 14px 22px rgba(0, 40, 50, 0.45);
    overflow: hidden;
  }
  .card__texture { position: absolute; inset: 0; width: 1050px; height: 600px; }
  .card__divider { position: absolute; left: 495px; top: 125px; width: 30px; height: 380px; }
  .brand {
    position: absolute; left: 60px; top: 368px; width: 420px;
    text-align: center;
  }
  .brand__name {
    font-weight: 500; font-size: 84px; letter-spacing: 10px; line-height: 1;
    color: var(--gold);
  }
  .brand__tagline {
    margin-top: -4px; color: var(--white);
    font-weight: 400; font-size: 26px; letter-spacing: 6.5px;
  }
  .holder {
    position: absolute; right: 58px; top: 88px;
    color: var(--white); font-size: 46px; letter-spacing: 1px; white-space: nowrap;
    text-align: right;
  }
  .holder__first { font-weight: 700; }
  .holder__last { font-weight: 300; }
  .contacts { position: absolute; left: 571px; top: 354px; list-style: none; }
  .contacts__item {
    display: flex; align-items: center; height: 34.5px;
    color: var(--white); font-size: 19px; font-weight: 400; white-space: nowrap;
  }
  .contacts__icon { width: 26px; height: 26px; margin-right: 14px; flex: none; }
</style>
</head>
<body>
<div class="canvas">
  <div class="card">
    <svg class="card__texture" viewBox="0 0 1050 600" role="img" aria-label="Fine teal line-fan texture along the top edge and left side of the card">
      <defs>
        <linearGradient id="texture-top" x1="0" y1="0" x2="0" y2="1">
          <stop offset="0" stop-color="var(--pattern-teal)" stop-opacity="0.75"/>
          <stop offset="1" stop-color="var(--pattern-deep)" stop-opacity="0.55"/>
        </linearGradient>
        <linearGradient id="texture-left" x1="0" y1="0" x2="1" y2="0">
          <stop offset="0" stop-color="var(--pattern-teal)" stop-opacity="0.7"/>
          <stop offset="1" stop-color="var(--pattern-deep)" stop-opacity="0.4"/>
        </linearGradient>
      </defs>
      <polygon points="0,0 1050,0 1050,175 525,62 0,170" fill="url(#texture-top)"/>
      <polygon points="0,0 100,60 45,300 110,600 0,600" fill="url(#texture-left)"/>
    </svg>

    <svg class="card__divider" viewBox="0 0 30 380" aria-hidden="true">
      <defs>
        <linearGradient id="divider-fade" x1="0" y1="0" x2="0" y2="1">
          <stop offset="0" stop-color="var(--silver)" stop-opacity="0"/>
          <stop offset="0.5" stop-color="var(--silver)" stop-opacity="1"/>
          <stop offset="1" stop-color="var(--silver)" stop-opacity="0"/>
        </linearGradient>
      </defs>
      <rect x="5" y="60" width="1.5" height="260" fill="url(#divider-fade)"/>
      <rect x="14" y="0" width="2" height="380" fill="url(#divider-fade)"/>
      <rect x="23" y="60" width="1.5" height="260" fill="url(#divider-fade)"/>
    </svg>

    <div class="brand">
      <div class="brand__name">VELTRA</div>
      <div class="brand__tagline">CLEVER LIVING</div>
    </div>

    <h1 class="holder"><span class="holder__first">DEREK</span> <span class="holder__last">HALLORAN</span></h1>

    <ul class="contacts">
      <li class="contacts__item">
        <svg class="contacts__icon" viewBox="0 0 26 26" aria-hidden="true">
          <circle cx="13" cy="13" r="13" fill="var(--white)"/>
          <path d="M8.5 7 l3 0 1 3.5 -1.8 1.4 a9 9 0 0 0 3.6 3.6 l1.4 -1.8 3.5 1 0 3 a1.5 1.5 0 0 1 -1.6 1.4 A11 11 0 0 1 7.1 8.6 1.5 1.5 0 0 1 8.5 7z" fill="var(--card-navy)"/>
        </svg>
        +34-602-518-794
      </li>
      <li class="contacts__item">
        <svg class="contacts__icon" viewBox="0 0 26 26" aria-hidden="true">
          <circle cx="13" cy="13" r="13" fill="var(--white)"/>
          <g fill="none" stroke="var(--card-navy)" stroke-width="1.4">
            <circle cx="13" cy="13" r="7"/>
            <ellipse cx="13" cy="13" rx="3" ry="7"/>
            <line x1="6" y1="13" x2="20" y2="13"/>
          </g>
        </svg>
        www.veltrasmarthomes.com
      </li>
      <li class="contacts__item">
        <svg class="contacts__icon" viewBox="0 0 26 26" aria-hidden="true">
          <circle cx="13" cy="13" r="13" fill="var(--white)"/>
          <rect x="6" y="8" width="14" height="10" rx="1" fill="var(--card-navy)"/>
          <path d="M6.5 8.5 L13 13.5 L19.5 8.5" fill="none" stroke="var(--white)" stroke-width="1.2"/>
        </svg>
        DHalloran@VELTRAsmarthomes.com
      </li>
      <li class="contacts__item">
        <svg class="contacts__icon" viewBox="0 0 26 26" aria-hidden="true">
          <circle cx="13" cy="13" r="13" fill="var(--white)"/>
          <path d="M13 5.5 a5.5 5.5 0 0 1 5.5 5.5 c0 4 -5.5 10 -5.5 10 s-5.5 -6 -5.5 -10 A5.5 5.5 0 0 1 13 5.5z" fill="var(--card-navy)"/>
          <circle cx="13" cy="11" r="2" fill="var(--white)"/>
        </svg>
        Plaza Brisa Local 42,Port Velamar, 07392
      </li>
    </ul>
  </div>
</div>
</body>
</html>
```